The Velvet Lantern Open Studio 5th Year

We need the creative direction for this year’s pop up gallery.
We are focusing on the themes of:
Empathy Compassion and Respect.
We will start with a flyer and use this as the basis for presentations and announcements. I would like to be able to include different logos of sponsors and names of other partners.

Target Market(s)

Art lovers and media industry

Industry/Entity Type

Art Gallery

Font styles to use
Sans Serif

Colors
000000
ec1f27
ffffff

Requirements
Must have
• TVLOPENSTUDIO
• The Velvet Lantern Open Studio
• Year 5 or 5th Year
• Canvas Harbor/Coastline Gallery Days 2018
• Dec 4-9
• TVLOPENSTUDIO.EXAMPLE
• EMPATHY COMPASSION RESPECT
Nice to have
• I would like to see simple bold and clear design
• NOT TOO BUSY
• NOT CLUTTERED
• CLEAN
• Maybe retro in layout
• With an idea of community coming together of different backgrounds
• But using red, black and white
Should not have
• Any graphics or images like people or any objects

```html
<!DOCTYPE html>
<html lang="en">
<head>
<meta charset="utf-8">
<title>Noise — The Velvet Lantern Open Studio</title>
<link rel="stylesheet" href="https://fonts.googleapis.com/css2?family=Anton&family=Montserrat:wght@700;800&display=swap">
<style>
  :root {
    --black: #0b0b0c;
    --red: #dd2622;
    --white: #ffffff;
    --stage: #8b9394;
    --paper-grey: #dededd;
    --shadow-grey: #a9a9a9;
  }
  * { margin: 0; padding: 0; box-sizing: border-box; }
  html, body { width: 1124px; height: 1200px; overflow: hidden; }
  body {
    background: var(--stage);
    font-family: "Montserrat", Arial, sans-serif;
    position: relative;
  }
  .flyer {
    position: absolute; left: 246px; top: 152px;
    width: 632px; height: 895px;
    background: linear-gradient(var(--paper-grey) 0 442px, var(--white) 442px);
    overflow: hidden;
  }
  .abs { position: absolute; }
  .corner-square { background: var(--black); }
  .corner-square--top { left: 0; top: 0; width: 64px; height: 70px; }
  .corner-square--bottom { left: 568px; top: 824px; width: 64px; height: 71px; }
  .corner-shapes { left: 0; top: 0; width: 632px; height: 895px; }

  .shadow { background: var(--shadow-grey); }
  .presenter-shadow { left: 113px; top: 48px; width: 306px; height: 106px; }
  .presenter {
    left: 91px; top: 33px; width: 306px; height: 106px;
    background: var(--black); padding: 20px 0 0 31px;
    font-weight: 800; font-size: 21px; line-height: 1.4; text-transform: uppercase;
  }
  .presenter__name { color: var(--red); display: block; white-space: nowrap; }
  .presenter__studio { color: var(--white); display: block; }
  .presents-shadow { left: 331px; top: 104px; width: 203px; height: 41px; }
  .presents {
    left: 310px; top: 88px; width: 203px; height: 41px;
    background: var(--white); border: 2px solid var(--black);
    font-weight: 800; font-size: 16px; color: var(--black);
    display: flex; align-items: center; justify-content: center;
    letter-spacing: 0.5px; white-space: nowrap;
  }
  .presents__year { color: var(--red); margin-right: 7px; }

  .title-shadow { left: 92px; top: 202px; width: 485px; height: 398px; }
  .title-dark { left: 70px; top: 184px; width: 487px; height: 201px; background: var(--black); }
  .title-light {
    left: 72px; top: 385px; width: 484px; height: 197px;
    background: var(--white); border: 2px solid var(--black); border-top: none;
  }
  .title-art { left: 0; top: 0; width: 632px; height: 600px; }
  .title-word { font-family: "Anton", Impact, sans-serif; font-size: 160px; }

  .city-mark { left: 104px; top: 614px; width: 205px; height: 64px; background: var(--black); }
  .event {
    left: 326px; top: 612px;
    font-weight: 800; font-size: 19px; line-height: 22px; color: var(--black);
    text-transform: uppercase; white-space: nowrap;
  }
  .dates {
    left: 55px; top: 700px; width: 523px; height: 74px;
    background: var(--paper-grey);
    display: flex; flex-direction: column; align-items: center; justify-content: center;
    color: var(--black);
  }
  .dates__range { font-weight: 800; font-size: 32px; line-height: 38px; }
  .dates__values {
    font-weight: 800; font-size: 13px; letter-spacing: 3px; color: var(--red);
    text-transform: uppercase;
  }
  .artist {
    left: 0; top: 780px; width: 632px;
    text-align: center; font-weight: 800; font-size: 58px; line-height: 70px; color: var(--red);
    text-transform: uppercase; letter-spacing: 1px;
  }
  .website {
    left: 0; top: 856px; width: 632px;
    text-align: center; font-weight: 800; font-size: 14px; letter-spacing: 1.5px; color: var(--black);
  }
</style>
</head>
<body>
  <main class="flyer">
    <svg class="abs corner-shapes" viewBox="0 0 632 895" aria-hidden="true">
      <polygon points="489,0 632,0 632,188" fill="#0b0b0c"/>
      <polygon points="0,768 98,895 0,895" fill="#0b0b0c"/>
      <polygon points="421,40 457,40 457,69" fill="#0b0b0c"/>
    </svg>
    <div class="abs corner-square corner-square--top"></div>
    <div class="abs corner-square corner-square--bottom"></div>

    <div class="abs shadow presenter-shadow"></div>
    <div class="abs presenter">
      <span class="presenter__name">The Velvet Lantern</span>
      <span class="presenter__studio">Open Studio</span>
    </div>
    <div class="abs shadow presents-shadow"></div>
    <div class="abs presents"><span class="presents__year">5TH YEAR</span>PRESENTS</div>

    <div class="abs shadow title-shadow"></div>
    <div class="abs title-dark"></div>
    <div class="abs title-light"></div>
    <svg class="abs title-art" viewBox="0 0 632 600" aria-label="Noise">
      <text class="title-word" x="189" y="350" textLength="250" lengthAdjust="spacingAndGlyphs" fill="#f2f2f2">NOISE</text>
      <text class="title-word" x="189" y="548" textLength="250" lengthAdjust="spacingAndGlyphs" fill="#0b0b0c">NOISE</text>
    </svg>

    <div class="abs city-mark" role="img" aria-label="City skyline silhouette above a red base line"></div>
    <div class="abs event">Canvas Harbor /<br>Coastline Gallery<br>Days 2018</div>

    <div class="abs dates">
      <span class="dates__range">Dec 4-9</span>
      <span class="dates__values">Empathy · Compassion · Respect</span>
    </div>
    <div class="abs artist">Dorian Vale</div>
    <div class="abs website">TVLOPENSTUDIO.EXAMPLE</div>
  </main>
</body>
</html>
```